New brand for digital company - your chance to get creative

We need to create a brand for our new business 'Lanternfish Digital'. Please read the brief below before progressing as we are looking for some quite specific outputs.

Background

We are positioning ourselves as ‘marketing technologists’ - we're helping businesses engage with their customers in the online space.

Our tactics include branding, marketing, online management, and social media, however we are differentiating ourselves by focusing on overall strategy, not just tactics. Our tagline is ‘Online made simple’.

We have stipulated some parameters for the brand but otherwise want designers to exercise their creativity.

Requirements
Must have
• We want to see an entire concept, not just a logo.

```html
<!DOCTYPE html>
<html lang="en">
<head>
<meta charset="utf-8">
<title>Lanternfish Digital — Brand Concept</title>
<link rel="stylesheet" href="https://fonts.googleapis.com/css2?family=Questrial&family=Open+Sans:wght@400;600;700&display=swap">
<style>
  :root {
    --orange: #f7860a;
    --orange-light: #fba55a;
    --orange-deep: #e0730a;
    --teal: #2ad6a0;
    --teal-light: #6ff0c4;
    --teal-deep: #1fbf8c;
    --grey: #9b9b9b;
    --grey-line: #a8a8a8;
    --grey-block: #d6d6d6;
    --grey-text: #5a5a5a;
    --ink: #3c3c3c;
    --paper: #ffffff;
  }
  * { margin: 0; padding: 0; box-sizing: border-box; }
  html, body { width: 1200px; height: 673px; overflow: hidden; background: var(--paper); }
  .canvas { position: relative; width: 1200px; height: 673px; overflow: hidden; font-family: "Questrial", sans-serif; }
  .abs { position: absolute; }

  /* brand lockup */
  .brand-square { left: 48px; top: 40px; width: 56px; height: 56px; background: var(--orange); }
  .brand-name { left: 122px; top: 36px; font-family: "Open Sans", sans-serif; font-weight: 600; font-size: 34px; color: var(--orange); white-space: nowrap; line-height: 1.2; }
  .tagline { left: 124px; top: 80px; font-family: "Open Sans", sans-serif; font-weight: 400; font-size: 17px; color: var(--grey-text); white-space: nowrap; line-height: 1.2; }

  /* image tiles */
  .tile { position: absolute; }
  .tile-stone { left: 333px; top: 137px; width: 141px; height: 143px; background: radial-gradient(circle at 40% 40%, #dcd9d5, #b4afaa 70%, #a29d97); }
  .tile-sky { left: 483px; top: 139px; width: 142px; height: 141px; background: linear-gradient(180deg, #21bd86, #3fd79e 70%, #62e6b2); }
  .tile-lights { left: 333px; top: 289px; width: 143px; height: 141px; background: radial-gradient(circle at 50% 45%, #1fc9a7, #0c4f5a 55%, #04121c); }
  .tile-photo-texture { left: 484px; top: 288px; width: 141px; height: 141px; background: var(--orange); border-radius: 11px; color: #fff; font-family: "Open Sans", sans-serif; font-weight: 700; font-size: 14px; padding: 98px 0 0 21px; white-space: nowrap; }

  /* quotes */
  .quote { color: var(--orange); line-height: 1; white-space: nowrap; }
  .q-small { font-size: 14px; }
  .q-big { font-size: 29px; }
  .q-mid { font-size: 22px; }
  .q-cite { font-size: 6px; }
  .connector { position: absolute; background: var(--grey-line); }
  .dot { position: absolute; width: 8px; height: 8px; border-radius: 50%; background: var(--grey); }

  .headline { color: var(--teal); font-size: 13px; white-space: nowrap; }
  .headline strong { font-weight: 400; font-size: 18px; }
  .body-copy { font-family: "Open Sans", sans-serif; font-size: 6.6px; line-height: 9px; color: var(--grey-text); }
  .body-copy em { font-style: normal; color: var(--teal); }
  .right { text-align: right; }

  /* bottom squares */
  .step { position: absolute; top: 618px; width: 24px; height: 24px; background: var(--grey-block); }
  .step.active { top: 612px; width: 34px; height: 34px; background: var(--orange); }

  /* text panel */
  .panel { left: 650px; top: 124px; width: 202px; height: 482px; border: 3px solid var(--grey-line); border-radius: 18px; background: var(--paper); }
  .panel-inner { position: absolute; left: 10px; top: 10px; right: 14px; bottom: 16px; border-radius: 12px; background: linear-gradient(180deg, #fff 50%, #efefef); }
  .panel-text { position: absolute; left: 19px; top: 26px; width: 166px; font-family: "Open Sans", sans-serif; font-weight: 600; font-size: 8.2px; line-height: 11.6px; color: var(--ink); }
  .panel-text p + p { margin-top: 11.6px; }

  /* service boxes */
  .service { width: 154px; height: 100px; border: 3px solid var(--grey-line); border-radius: 10px; background: var(--paper); }
  .service-inner { position: absolute; left: 9px; top: 8px; right: 10px; bottom: 10px; border-radius: 8px; background: linear-gradient(135deg, #fff 30%, #e6e6e6); }
  .service-title { position: absolute; left: 20px; top: 12px; font-family: "Open Sans", sans-serif; font-weight: 700; font-size: 18px; color: var(--orange); white-space: nowrap; }

  .people-title { left: 862px; top: 543px; font-family: "Open Sans", sans-serif; font-weight: 700; font-size: 18px; color: var(--orange); }
  .people-grid { left: 862px; top: 570px; display: grid; grid-template-columns: repeat(4, 42px); grid-auto-rows: 42px; gap: 1px; }
  .people-grid span { background: linear-gradient(160deg, #6a5a52, #2c2a33); }

  .swatch { left: 1050px; top: 568px; width: 110px; height: 78px; display: grid; grid-template-columns: 24px 62px 24px; grid-template-rows: 10px 20px 9px 10px 9px 20px; }

  .cube { position: absolute; width: 36px; height: 36px; background: var(--grey-block); }
  .cube.orange { background: var(--orange); }
  .cube.teal { background: var(--teal-light); }
</style>
</head>
<body>
<div class="canvas">

  <!-- brand lockup -->
  <div class="abs brand-square"></div>
  <div class="abs brand-name">Lanternfish Digital</div>
  <div class="abs tagline">online made simple</div>

  <!-- image tiles -->
  <div class="tile tile-stone" role="img" aria-label="Close-up of pale grey marble stone texture"></div>
  <div class="tile tile-sky" role="img" aria-label="White clouds on a green sky"></div>
  <div class="tile tile-lights" role="img" aria-label="Coiled glowing teal rope lights on a dark background"></div>
  <div class="tile tile-photo-texture">...photo texture</div>

  <!-- first quote -->
  <div class="abs quote q-small" style="left:64px;top:214px;">“a brand becomes</div>
  <div class="abs quote q-big" style="left:56px;top:227px;">stronger</div>
  <div class="abs quote" style="left:76px;top:255px;font-size:12px;">when you</div>
  <div class="abs quote q-mid" style="left:64px;top:265px;">narrow the focus.”<span class="q-cite"> – jo renner</span></div>
  <div class="dot" style="left:191px;top:218px;"></div>
  <div class="connector" style="left:197px;top:221px;width:136px;height:2px;"></div>

  <div class="abs headline" style="left:53px;top:296px;">our marketing is <strong>creative</strong>.</div>
  <div class="abs body-copy" style="left:53px;top:322px;width:222px;">our marketing approach is <em>focused on visual excellence</em>. this creates highly targeted design. as a result, the marketing is more effective with a higher ratio of conversions. our creative expertise and aesthetic philosophy is an integral part of our marketing strategy.</div>

  <!-- second quote -->
  <div class="abs quote q-mid" style="left:162px;top:386px;"><span style="font-size:12px;">“</span>brand is</div>
  <div class="abs quote" style="left:155px;top:408px;font-size:12px;">not what you say it is.</div>
  <div class="abs quote" style="left:175px;top:421px;font-size:12px;">it's <span style="font-size:17px;">what</span></div>
  <div class="abs quote" style="left:161px;top:434px;font-size:22px;">they <span style="font-size:15px;">say it is ”</span></div>
  <div class="abs quote q-cite" style="left:247px;top:460px;">– the signal book</div>
  <div class="dot" style="left:312px;top:460px;"></div>
  <div class="connector" style="left:318px;top:463px;width:83px;height:2px;"></div>
  <div class="connector" style="left:399px;top:430px;width:2px;height:35px;"></div>

  <div class="abs headline right" style="left:89px;top:477px;width:218px;">our marketing is <strong>brand focused</strong>.</div>
  <div class="abs body-copy right" style="left:85px;top:505px;width:222px;">we are committed to understanding the brand's positioning before the beginning of any project.</div>
  <div class="abs body-copy right" style="left:85px;top:529px;width:222px;">we study the objective and current position of the brand and refine it, or reposition if necessary. we do this in order to make the marketing efforts <em>clear, focused and effectively understood</em>.</div>

  <!-- bottom progress squares -->
  <div class="step" style="left:212px;"></div>
  <div class="step" style="left:240px;"></div>
  <div class="step" style="left:268px;"></div>
  <div class="step" style="left:296px;"></div>
  <div class="step active" style="left:328px;"></div>
  <div class="step" style="left:366px;"></div>
  <div class="step" style="left:394px;"></div>
  <div class="step" style="left:422px;"></div>

  <!-- connectors to panel and services -->
  <div class="connector" style="left:795px;top:0;width:2px;height:126px;"></div>
  <div class="connector" style="left:806px;top:0;width:2px;height:126px;"></div>
  <div class="connector" style="left:851px;top:365px;width:73px;height:2px;"></div>
  <div class="connector" style="left:851px;top:375px;width:73px;height:2px;"></div>
  <div class="connector" style="left:851px;top:500px;width:73px;height:2px;"></div>

  <!-- text panel -->
  <div class="abs panel">
    <div class="panel-inner"></div>
    <div class="panel-text">
      <p>Lorem ipsum dolor sit amet, consectetur adipiscing elit. Integer molestie arcu nec enim vehicula ornare. Aenean facilisis nisi sit amet lacus adipiscing fringilla. Nam molestie justo at diam pretium a placerat sem fringilla Nam aliquam, lacus nec porta bibendum, ante lorem aliquet nunc, nec sagittis lorem ante a ante. Praesent felis augue, pulvinar ac vestibulum id, congue a ipsum. Praesent rhoncus ante nec augue cursus semper. Donec ut arcu ut massa accumsan aliquet quis id mi. Nullam non odio purus, at mollis quam. Sed sit amet nunc at lectus facilisis semper eu convallis mi. Morbi purus erat, facilisis eget auctor in, ultrices eget magna. Cras neque nunc, tempor vel facilisis at, egestas vel nibh.</p>
      <p>Mauris ipsum mauris, venenatis sed tincidunt rutrum, mollis in risus. Duis convallis lectus felis, adipiscing consequat nulla. Phasellus at diam nec sapien feugiat euismod at fermentum dolor. Vestibulum erat arcu, scelerisque ut tempus eu, sagittis vitae metus. Sed vestibulum mauris quis facilisis. Donec ac venenatis odio. Mauris lacinia mi placerat tortor eleifend elementum vestibulum est porttitor. Aliquam erat volutpat.</p>
    </div>
  </div>

  <!-- decorative squares -->
  <div class="cube" style="left:876px;top:0;"></div>
  <div class="cube" style="left:876px;top:24px;"></div>
  <div class="cube" style="left:912px;top:34px;"></div>
  <div class="cube" style="left:950px;top:48px;"></div>
  <div class="cube" style="left:1084px;top:36px;"></div>
  <div class="cube" style="left:1084px;top:76px;"></div>
  <div class="cube" style="left:1084px;top:116px;"></div>
  <div class="cube" style="left:1084px;top:156px;"></div>
  <div class="cube orange" style="left:898px;top:116px;"></div>
  <div class="cube" style="left:898px;top:160px;"></div>
  <div class="cube" style="left:966px;top:186px;"></div>
  <div class="cube" style="left:998px;top:172px;"></div>
  <div class="cube" style="left:998px;top:212px;"></div>
  <div class="cube" style="left:1032px;top:228px;"></div>
  <div class="cube" style="left:1064px;top:214px;"></div>
  <div class="cube teal" style="left:1064px;top:256px;"></div>
  <div class="cube" style="left:966px;top:256px;"></div>
  <div class="cube" style="left:966px;top:298px;"></div>
  <div class="cube" style="left:1070px;top:372px;"></div>
  <div class="cube" style="left:1104px;top:386px;"></div>
  <div class="cube" style="left:1130px;top:390px;"></div>
  <div class="cube" style="left:1164px;top:406px;"></div>

  <!-- services -->
  <div class="abs service" style="left:922px;top:324px;">
    <div class="service-inner"></div>
    <div class="service-title">marketing</div>
  </div>
  <div class="abs service" style="left:922px;top:437px;">
    <div class="service-inner"></div>
    <div class="service-title" style="left:17px;">management</div>
  </div>

  <!-- people -->
  <div class="abs people-title">people</div>
  <div class="abs people-grid" role="img" aria-label="Grid of eight team member portrait photos">
    <span></span><span></span><span></span><span></span>
    <span></span><span></span><span></span><span></span>
  </div>

  <!-- colour swatch -->
  <div class="abs swatch" aria-hidden="true">
    <span style="background:var(--orange-light)"></span><span style="background:var(--orange)"></span><span style="background:var(--orange-deep)"></span>
    <span style="background:var(--orange-light)"></span><span style="background:var(--orange)"></span><span style="background:var(--orange-deep)"></span>
    <span style="background:var(--teal-light)"></span><span style="background:var(--teal)"></span><span style="background:var(--teal-deep)"></span>
    <span style="background:var(--teal-light)"></span><span style="background:var(--teal)"></span><span style="background:var(--teal-deep)"></span>
    <span style="background:#c9c9c9"></span><span style="background:#a9a9a9"></span><span style="background:#8e8e8e"></span>
    <span style="background:#dcdcdc"></span><span style="background:#b5b5b5"></span><span style="background:#c4c4c4"></span>
  </div>

</div>
</body>
</html>
```